Business Card Design Project

Hi,
This is a simple contest. The logo for the back of the card is deigned. See attached files. The front of the card must have :

Directors Name: Tobias
Mob:
e-mail:
Postal Address:
Web Page Adress:

It may also add words: "Leaders in Construction Project Management Services"

Target Market(s)

Business & Home owners alike

Industry/Entity Type

Business

Requirements
Must have
• See details above and logo attached
Should not have
• Images other than logo

```html
<!DOCTYPE html>
<html lang="en">
<head>
<meta charset="utf-8">
<title>Corvale Build Partners – Business Card</title>
<link rel="stylesheet" href="https://fonts.googleapis.com/css2?family=Arimo:wght@400;700&display=swap">
<style>
  :root {
    --brand-blue: #00a0dc;
    --paper: #ffffff;
    --ink: #000000;
  }
  * { margin: 0; padding: 0; box-sizing: border-box; }
  html, body {
    width: 1039px;
    height: 1200px;
    overflow: hidden;
    background: var(--paper);
    font-family: "Arimo", Arial, sans-serif;
  }
  .sheet {
    position: relative;
    width: 1039px;
    height: 1200px;
    background: var(--paper);
  }

  /* Card back: solid brand panel with company name */
  .card-back {
    position: absolute;
    left: 29px;
    top: 23px;
    width: 981px;
    height: 542px;
    background: var(--brand-blue);
    display: flex;
    align-items: center;
    justify-content: center;
  }
  .brand-name {
    color: var(--paper);
    font-weight: 700;
    font-size: 54px;
    letter-spacing: 2px;
    white-space: nowrap;
  }

  /* Card front: blue frame around white face */
  .card-front {
    position: absolute;
    left: 0;
    top: 600px;
    width: 1039px;
    height: 600px;
    background: var(--brand-blue);
  }
  .card-face {
    position: absolute;
    left: 29px;
    top: 26px;
    width: 981px;
    height: 542px;
    background: var(--paper);
  }
  .rule {
    position: absolute;
    left: 35px;
    height: 4px;
    background: var(--ink);
  }
  .rule--top { top: 83px; width: 606px; }
  .rule--bottom { top: 402px; width: 483px; }

  .contact-list {
    position: absolute;
    left: 35px;
    top: 112px;
    list-style: none;
    font-size: 39px;
    line-height: 55px;
    color: var(--ink);
    white-space: nowrap;
  }
  .contact-label {
    color: var(--brand-blue);
    font-weight: 700;
  }

  .face-brand {
    position: absolute;
    right: 72px;
    top: 316px;
    color: var(--brand-blue);
    font-weight: 700;
    font-size: 36px;
    letter-spacing: 1px;
  }

  .tagline {
    position: absolute;
    left: 35px;
    top: 490px;
    font-size: 25px;
    font-weight: 700;
    color: var(--ink);
    white-space: nowrap;
  }
</style>
</head>
<body>
  <main class="sheet">
    <section class="card-back">
      <span class="brand-name">CORVALE BUILD PARTNERS</span>
    </section>

    <section class="card-front">
      <div class="card-face">
        <div class="rule rule--top"></div>
        <ul class="contact-list">
          <li><span class="contact-label">DIRECTORS NAME:</span> YOUR NAME</li>
          <li><span class="contact-label">MOB</span><span class="contact-label" style="font-weight:400">:</span> (000) 000 - 000</li>
          <li><span class="contact-label">E-MAIL</span><span class="contact-label" style="font-weight:400">:</span> YOUR@EMAIL.COM</li>
          <li><span class="contact-label">ADDRESS</span><span class="contact-label" style="font-weight:400">:</span> YOUR ADRES 0</li>
          <li><span class="contact-label">WEB:</span> YOURWEBSITE.COM</li>
        </ul>
        <div class="rule rule--bottom"></div>
        <span class="face-brand">CORVALE</span>
        <p class="tagline">LEADERS IN CONSTRUCTION PROJECT MANAGEMENT SERVICES</p>
      </div>
    </section>
  </main>
</body>
</html>
```